Belle & Veil Studio Expert 5 page Website

Modern 5 page website including: home page, Bridal Experts, services, gallery, and book me. Home page to include photo slideshow and contact information for stylist. The Bridal a Experts section will include short biography and photos of each bridal expert 3-4. Services page will include list and description of services and pricing. Gallery will contain work divided in the hair and makeup category. The book me page will contain an active booking tab with drop down service and customer information.

Target Market(s)

Brides, ages 21 to 45

Industry/Entity Type

Hair And Beauty

Coding

Coded - Design and coding required

Number of Pages Required

5+ page

Font styles to use
Serif
Decorative
Script

Colors
faa54b
97b8d9

Requirements
Must have
• Photo slideshow, photo gallery
Nice to have
• Scrolling slide show on home page

```html
<!DOCTYPE html>
<html lang="en">
<head>
<meta charset="utf-8">
<title>Belle &amp; Veil — Packages</title>
<link rel="stylesheet" href="https://fonts.googleapis.com/css2?family=Open+Sans:ital,wght@0,400;0,600;0,700;1,400&family=Great+Vibes&display=swap">
<style>
:root{
  --teal:#8ccfca;
  --teal-dark:#6fbdb8;
  --teal-deep:#5aa7a6;
  --orange:#f9a04a;
  --orange-deep:#f78a2e;
  --ink:#444;
  --muted:#666;
  --line:#e6e6e6;
  --page:#f7f7f7;
  --white:#fff;
}
*{box-sizing:border-box;margin:0;padding:0}
html,body{width:748px;height:1200px;overflow:hidden}
body{position:relative;background:var(--page);font-family:'Open Sans',sans-serif;color:var(--ink)}
.abs{position:absolute}
.topbar{left:0;top:0;width:748px;height:27px;background:linear-gradient(#9ad8d3,var(--teal-dark));color:#fff;font-size:8px}
.topbar .contact{left:54px;top:9px;display:flex;gap:16px}
.topbar .social{right:54px;top:5px;display:flex;gap:4px}
.ring{width:17px;height:17px;border:1px solid #fff;border-radius:50%}
.header{left:0;top:27px;width:748px;height:59px;background:var(--white)}
.hero{left:0;top:86px;width:748px;height:197px;background:linear-gradient(100deg,#8f8574,#b7ab94 40%,#a59c8b 70%,#8b8a84);z-index:1}
.logo-oval{left:56px;top:30px;width:168px;height:105px;border-radius:50%;background:var(--white);box-shadow:0 2px 4px rgba(0,0,0,.1);display:flex;align-items:center;justify-content:center;z-index:5}
.logo-oval.footer-logo{left:53px;top:1040px;width:160px;height:100px;background:transparent;box-shadow:none;border:2px solid rgba(255,255,255,.85)}
.logo-inner{width:130px;height:66px;border-radius:50%;border:3px solid var(--teal);display:flex;align-items:center;justify-content:center;font-size:13px;font-weight:600;color:var(--teal-deep)}
.footer-logo .logo-inner{border-color:#fff;color:#fff}
.nav{top:54px;left:280px;display:flex;font-size:7.5px;color:#333}
.nav span{margin-right:25px}
.nav .active{color:var(--orange)}
.nav-icon{top:45px;width:23px;height:23px;border-radius:50%;border:1px solid var(--orange)}
.nav-icon.cal{border-color:var(--teal)}
.ornament{left:282px;top:327px;width:186px;height:1px;background:#777}
.title{left:0;width:748px;top:336px;text-align:center;font-family:'Great Vibes',cursive;font-size:26px;font-weight:400;color:var(--orange)}
.intro{left:120px;width:508px;top:378px;text-align:center;font-size:7.3px;font-style:italic;line-height:15px;color:#555;white-space:nowrap}
.card{width:201px;height:262px;background:var(--white);border:1px solid var(--line);box-shadow:0 1px 2px rgba(0,0,0,.05)}
.card .photo{position:absolute;left:6px;top:5px;width:189px;height:141px;border-radius:2px}
.card h3{position:absolute;left:6px;top:160px;font-size:10.5px;font-weight:400;color:#333}
.card .stars{position:absolute;right:10px;top:162px;display:flex;gap:1px}
.card p{position:absolute;left:6px;top:182px;width:192px;font-size:6.8px;font-style:italic;line-height:15px;color:#666;white-space:nowrap}
.card .price{position:absolute;left:6px;top:234px;font-size:11.5px;font-weight:700;color:var(--orange)}
.card .more{font-size:9px;font-weight:600}
.card.featured{background:linear-gradient(var(--orange),var(--orange-deep));border-color:var(--orange)}
.card.featured h3,.card.featured p,.card.featured .price{color:#fff}
.footer{left:0;top:1007px;width:748px;height:193px;background:linear-gradient(#9ad8d3,var(--teal-deep));color:#fff}
.fhead{font-family:'Great Vibes',cursive;font-size:20px;color:#fff}
.flist{font-size:7px;line-height:18px}
.flist div{display:flex;align-items:center;gap:10px}
.email-field{width:148px;height:20px;background:#fff;color:#555;font-size:7.5px;padding:5px 10px}
.subscribe{width:50px;height:16px;background:var(--teal-deep);font-size:6.5px;text-align:center;line-height:16px}
.fsocial{display:flex;gap:5px}
.fsocial .ring{width:22px;height:22px}
.copyright{left:0;width:748px;top:1175px;text-align:center;font-size:7.3px}
</style>
</head>
<body>
<div class="abs topbar">
  <div class="abs contact"><span>☏ Call us : (000)-555-0142</span><span>✉ Email : hello@belleandveil.com</span></div>
  <div class="abs social"><div class="ring"></div><div class="ring"></div><div class="ring"></div><div class="ring"></div></div>
</div>
<div class="abs header"></div>
<nav class="abs nav"><span>HOME</span><span>BRIDAL EXPERTS</span><span class="active">PACKAGES</span><span>GALLERY</span><span>BOOK ME</span><span>CONTACT US</span></nav>
<div class="abs nav-icon" style="left:644px">
  <svg width="21" height="21" viewBox="0 0 21 21"><circle cx="9.5" cy="9.5" r="3" fill="none" stroke="#f9a04a"/><path d="M11.7 11.7l2.5 2.5" stroke="#f9a04a"/></svg>
</div>
<div class="abs nav-icon cal" style="left:671px">
  <svg width="21" height="21" viewBox="0 0 21 21"><rect x="7" y="7" width="7" height="7" fill="none" stroke="#8ccfca"/><path d="M7 9h7" stroke="#8ccfca"/></svg>
</div>

<div class="abs hero" role="img" aria-label="Hero photo of a bridal couple resting in a dry grass field"></div>
<div class="abs logo-oval"><div class="logo-inner">Belle &amp; Veil</div></div>

<div class="abs ornament"></div>
<h2 class="abs title">Our Services</h2>
<p class="abs intro">It is a long established fact that a reader will be distracted by the readable content of a page when looking at its layout. The point of<br>using Lorem -or-less normal distribution of letters, as opposed to using 'Contenteadable English.</p>

<svg width="0" height="0" style="position:absolute"><defs><symbol id="star" viewBox="0 0 10 10"><path d="M5 .8l1.2 2.7 2.9.3-2.2 1.9.7 2.9L5 7.1 2.4 8.6l.7-2.9L.9 3.8l2.9-.3z" fill="none" stroke="currentColor" stroke-width=".9"/></symbol></defs></svg>

<div class="abs card featured" style="left:53px;top:430px">
  <div class="photo" role="img" aria-label="Photo of a bride having her makeup applied" style="background:linear-gradient(120deg,#a58a78,#d9c2b0 50%,#8d6d5b)"></div>
  <h3>Blissful luxe</h3>
  <div class="stars" style="color:#fff"><svg width="8" height="8"><use href="#star"/></svg><svg width="8" height="8"><use href="#star"/></svg><svg width="8" height="8"><use href="#star"/></svg><svg width="8" height="8"><use href="#star"/></svg><svg width="8" height="8"><use href="#star"/></svg></div>
  <p>Sed ut perspiciatis unde omnis iste natus error sit volup-<br>tatem accusantium doloremque laudantium, totam rem<br>dolores eos qui ratione voluptatem</p>
  <div class="price">$435</div>
</div>
<div class="abs card" style="left:273px;top:430px">
  <div class="photo" role="img" aria-label="Photo of a bride with curly hair getting blush applied" style="background:linear-gradient(120deg,#e2cdb5,#c7a98c 50%,#8a7667)"></div>
  <h3>Signature Beauty</h3>
  <div class="stars" style="color:var(--orange)"><svg width="8" height="8"><use href="#star"/></svg><svg width="8" height="8"><use href="#star"/></svg><svg width="8" height="8"><use href="#star"/></svg><svg width="8" height="8"><use href="#star"/></svg><svg width="8" height="8" style="color:#555"><use href="#star"/></svg></div>
  <p>Sed ut perspiciatis unde omnis iste natus error sit volup-<br>tatem accusantium doloremque laudantium, totam rem<br>dolores eos qui ratione voluptatem</p>
  <div class="price">$222</div>
</div>
<div class="abs card" style="left:493px;top:430px">
  <div class="photo" role="img" aria-label="Photo of a bride in a veil holding a bouquet" style="background:linear-gradient(100deg,#c9c0b4,#e8ded3 45%,#6e8a45)"></div>
  <h3>Simply makeup</h3>
  <div class="stars" style="color:var(--orange)"><svg width="8" height="8"><use href="#star"/></svg><svg width="8" height="8"><use href="#star"/></svg><svg width="8" height="8"><use href="#star"/></svg><svg width="8" height="8"><use href="#star"/></svg><svg width="8" height="8" style="color:#555"><use href="#star"/></svg></div>
  <p>Sed ut perspiciatis unde omnis iste natus error sit volup-<br>tatem accusantium doloremque laudantium, totam rem<br>dolores eos qui ratione voluptatem</p>
  <div class="price">$100</div>
</div>

<div class="abs card" style="left:53px;top:709px">
  <div class="photo" role="img" aria-label="Photo of a woman brushing her hair at a mirror" style="background:linear-gradient(100deg,#5a3b2d,#b08a72 50%,#e8e2dc)"></div>
  <h3>Simply Hair</h3>
  <div class="stars" style="color:var(--orange)"><svg width="8" height="8"><use href="#star"/></svg><svg width="8" height="8"><use href="#star"/></svg><svg width="8" height="8"><use href="#star"/></svg><svg width="8" height="8"><use href="#star"/></svg><svg width="8" height="8" style="color:#555"><use href="#star"/></svg></div>
  <p>Sed ut perspiciatis unde omnis iste natus error sit volup-<br>tatem accusantium doloremque laudantium, totam rem<br>dolores eos qui ratione voluptatem</p>
  <div class="price">$105</div>
</div>
<div class="abs card" style="left:273px;top:709px">
  <div class="photo" role="img" aria-label="Photo of a glamorous woman before festive bokeh lights" style="background:linear-gradient(100deg,#d8c3b0,#9c7d5c 55%,#4a4a2a)"></div>
  <h3>Bridal Glam</h3>
  <div class="stars" style="color:var(--orange)"><svg width="8" height="8"><use href="#star"/></svg><svg width="8" height="8"><use href="#star"/></svg><svg width="8" height="8"><use href="#star"/></svg><svg width="8" height="8"><use href="#star"/></svg><svg width="8" height="8" style="color:#555"><use href="#star"/></svg></div>
  <p>Sed ut perspiciatis unde omnis iste natus error sit volup-<br>tatem accusantium doloremque laudantium, totam rem<br>dolores eos qui ratione voluptatem</p>
  <div class="price">$200</div>
</div>
<div class="abs card" style="left:493px;top:709px">
  <div class="photo" role="img" aria-label="Photo of a wedding table setting with flowers and lanterns" style="background:linear-gradient(180deg,#7f8f6a,#c6a7a8 50%,#6d8a4e)"></div>
  <h3>OTHERS</h3>
  <div class="stars" style="color:var(--orange)"><svg width="8" height="8"><use href="#star"/></svg><svg width="8" height="8"><use href="#star"/></svg><svg width="8" height="8"><use href="#star"/></svg><svg width="8" height="8"><use href="#star"/></svg><svg width="8" height="8" style="color:#555"><use href="#star"/></svg></div>
  <p>Sed ut perspiciatis unde omnis iste natus error sit volup-<br>tatem accusantium doloremque laudantium, totam rem<br>dolores eos qui ratione voluptatem</p>
  <div class="price more">View More</div>
</div>

<footer class="abs footer"></footer>
<div class="abs logo-oval footer-logo"><div class="logo-inner">Belle &amp; Veil</div></div>

<div class="abs" style="left:245px;top:1030px">
  <div class="fhead">Contact Us</div>
  <div class="flist" style="color:#fff;margin-top:6px">
    <div><svg width="8" height="8" viewBox="0 0 8 8"><rect x="1" y="2" width="6" height="5" fill="#fff"/><rect x="0" y="1" width="8" height="2" rx="1" fill="#fff"/></svg>(000)-555-0142 (Phone)</div>
    <div><svg width="8" height="8" viewBox="0 0 8 8"><rect x="2" y="0" width="4" height="3" fill="#fff"/><rect x="0" y="3" width="8" height="4" fill="#fff"/></svg>(000)-555-0143 (Fax)</div>
    <div><svg width="8" height="8" viewBox="0 0 8 8"><rect x="0" y="1.5" width="8" height="5" fill="#fff"/></svg><u>studio@belleandveil.com</u></div>
    <div style="line-height:9px;margin-top:4px"><svg width="8" height="10" viewBox="0 0 8 10"><path d="M4 10L1 5a3 3 0 1 1 6 0z" fill="#fff"/></svg><span># 2658 Lorem ipsum Dummy<br>Lorem Ipsum</span></div>
  </div>
</div>

<div class="abs" style="left:390px;top:1030px;width:150px">
  <div class="fhead">Newsletter Signup</div>
  <p style="font-size:7px;line-height:13px;margin-top:8px">Register Your email address to get information about us</p>
  <div class="email-field" style="margin-top:10px">Email Address</div>
  <div class="subscribe" style="margin-top:6px">SUBSCRIBE</div>
</div>

<div class="abs" style="left:565px;top:1030px;width:130px">
  <div class="fhead">Follow Us</div>
  <p style="font-size:6.5px;line-height:12px;margin-top:8px">Lorem ipsum dolor sit amet, conse ctetur adipiscing elit. Nulla in purus nibh. Donec ornare</p>
  <div class="fsocial" style="margin-top:10px"><div class="ring"></div><div class="ring"></div><div class="ring"></div><div class="ring"></div><div class="ring"></div></div>
</div>

<div class="abs copyright" style="color:#fff">© Copyright 2016 Belle &amp; Veil Studio  All Rights Reserved</div>
</body>
</html>
```